Music Business Adviser Needs a Book Cover Design

I need a cover design for my new book called 'The Stage Performer: A Working Handbook for Launching Your Trade'. I am an accountant and tax lawyer specialising in advising international music artists. This book is designed to help music artists and bands navigate through the business world. I would like to see designs that would appeal to young artists, the book needs to be bold and stand out from the crowd, for example it will attract people on Bookvale through its enticing cover.

I am open to you providing creative input on the design, although I like the colour green and think this would perhaps communicate subtly financial safety and growth. The cover should clearly communicate the book is for people in the music industry.

Target Market(s)

Males and females aged between 16 and 30; their hobbies and interest are music; they perform and record music; all genres of music

Industry/Entity Type

Lawyer

Font styles to use
Sans Serif

Requirements
Must have
• Must have the title clearly stated: 'The Stage Performer: A Working Handbook for Launching Your Trade'. It must also have my name as author on the front: 'Gareth L. Quinby'
Nice to have
• I have uploaded an image of the type of artwork, that should be on the book. I like this style - so please keep it simple, not an over complicated design.
Should not have
• Photographs of bands or musicians

```html
<!DOCTYPE html>
<html lang="en">
<head>
<meta charset="utf-8">
<title>The Stage Performer — Book Cover</title>
<link rel="stylesheet" href="https://fonts.googleapis.com/css2?family=Oswald:wght@500&family=Crimson+Text:ital,wght@0,400;1,400&display=swap">
<style>
  :root {
    --backdrop: #e9ebea;
    --paper: #ffffff;
    --green: #2eaa72;
    --green-soft: #8fd3b0;
    --ink: #111111;
    --ink-soft: #555555;
  }
  * { box-sizing: border-box; margin: 0; padding: 0; }
  html, body {
    width: 1200px;
    height: 900px;
    overflow: hidden;
    background: var(--backdrop);
  }
  .stage {
    width: 1200px;
    height: 900px;
    display: flex;
    align-items: center;
    justify-content: center;
  }
  .cover {
    position: relative;
    width: 476px;
    height: 840px;
    background: var(--paper);
    box-shadow: 0 10px 30px rgba(0,0,0,0.12);
    overflow: hidden;
  }
  .cover__spine-band {
    position: absolute;
    left: 0; top: 0; bottom: 0;
    width: 16px;
    background: var(--green);
  }
  .cover__author {
    position: absolute;
    top: 46px;
    left: 0; right: 0;
    text-align: center;
    font-family: "Crimson Text", Georgia, serif;
    font-size: 25px;
    color: var(--ink);
    letter-spacing: 0.2px;
  }
  .cover__author-rule {
    position: absolute;
    top: 84px;
    left: 138px;
    width: 216px;
    height: 7px;
  }
  .cover__crest {
    position: absolute;
    top: 96px;
    left: 218px;
    width: 56px;
    height: 74px;
    border-radius: 40% 40% 50% 50%;
    background: radial-gradient(circle at 50% 45%, var(--green-soft), #cfe9dc 70%, var(--paper));
  }
  .cover__title {
    position: absolute;
    top: 250px;
    left: 16px; right: 0;
    text-align: center;
    font-family: "Oswald", "Arial Narrow", sans-serif;
    font-weight: 500;
    font-size: 52px;
    color: var(--green);
    transform: scaleY(1.08);
    letter-spacing: 0.3px;
  }
  .cover__subtitle {
    position: absolute;
    top: 362px;
    left: 16px; right: 0;
    text-align: center;
    font-family: "Crimson Text", Georgia, serif;
    font-style: italic;
    font-size: 36px;
    line-height: 1.35;
    color: var(--ink);
  }
  .cover__artwork {
    position: absolute;
    left: 170px;
    right: 0;
    top: 530px;
    bottom: 0;
    background: linear-gradient(160deg, #d6efe2 0%, var(--green-soft) 35%, #4a6a5a 70%, var(--ink) 100%);
    border-radius: 48% 0 0 0;
  }
</style>
</head>
<body>
  <main class="stage">
    <section class="cover">
      <div class="cover__spine-band"></div>
      <p class="cover__author">Gareth L. Quinby</p>
      <svg class="cover__author-rule" viewBox="0 0 216 7" aria-hidden="true">
        <rect x="0" y="0" width="216" height="2" fill="#111111"/>
        <rect x="0" y="4" width="216" height="3" fill="#111111"/>
      </svg>
      <div class="cover__crest" role="img" aria-label="Small ornamental motif of musical notes growing like a tree"></div>
      <h1 class="cover__title">The Stage Performer</h1>
      <p class="cover__subtitle">A Working Handbook for<br>Launching Your Trade</p>
      <div class="cover__artwork" role="img" aria-label="Illustration of a silhouetted head in profile with swirling green and black musical notes rising like foliage"></div>
    </section>
  </main>
</body>
</html>
```